Pediatric Dental Practice needs a postcard for direct mail advertising

We are looking for a creative and professional double-sided postcard design for a direct mail marketing campaign. Our goal is to attract new families to our pediatric dental practice by conveying a sense of warmth, modern care, and clinical excellence. The design should feel "boutique" and high-end yet remain fun and approachable for parents and children.

```html
<!DOCTYPE html>
<html lang="en">
<head>
<meta charset="utf-8">
<title>Birchwood Pediatric Dentistry – Postcard</title>
<link href="https://fonts.googleapis.com/css2?family=Poppins:wght@400;500;600;700&display=swap" rel="stylesheet">
<style>
  :root{
    --green-deep:#2a7f47;
    --green:#3a9a58;
    --green-mid:#5cae6d;
    --green-light:#8fcb8c;
    --mint:#b8e0b0;
    --ink:#1f2a22;
    --paper:#ffffff;
    --backdrop:#e6e7e8;
    --rule:#333;
  }
  *{box-sizing:border-box;margin:0;padding:0}
  html,body{width:1040px;height:1200px;overflow:hidden;background:var(--backdrop);font-family:'Poppins',sans-serif;color:var(--ink)}
  .card{position:absolute;left:100px;width:840px;height:560px;background:var(--paper);overflow:hidden;box-shadow:0 4px 14px rgba(0,0,0,.12)}
  .card--front{top:27px}
  .card--back{top:613px}
  .abs{position:absolute}

  /* brand block */
  .brand{display:flex;flex-direction:column;align-items:center;gap:6px;color:var(--green);font-weight:500;text-align:center;line-height:1.15}
  .brand-dot{width:30px;height:30px;border-radius:50%;background:var(--green-light);flex:none}
  .brand-name{font-size:15px}
  .brand--front{left:26px;top:18px;width:150px}
  .brand--back{left:590px;top:24px;width:190px}
  .brand--back .brand-dot{width:36px;height:36px}
  .brand--back .brand-name{font-size:18px}

  /* front */
  .hero-bg{left:0;top:0}
  .headline{left:36px;top:110px;color:#fff;font-weight:700;font-size:48px;line-height:56px;letter-spacing:.5px}
  .subhead{left:36px;top:252px;width:500px;color:#fff;font-weight:600;font-size:14px;line-height:22px}
  .intro{left:36px;top:306px;width:490px;color:#fff;font-size:10.5px;line-height:14px}
  .doctor{left:575px;top:22px;width:250px;height:340px;border-radius:120px 120px 0 60px;background:linear-gradient(180deg,#c9ddd9 0%,#aac9d8 55%,#8fb6c9 100%)}
  .network-title{left:36px;top:379px;color:var(--green);font-weight:600;font-size:13.5px}
  .providers{top:405px;list-style:none;font-size:9.6px;font-weight:500;line-height:14.2px}
  .providers li::before{content:"• ";}
  .providers--a{left:36px}
  .providers--b{left:282px}
  .contact-panel{left:540px;top:404px;width:300px;height:156px;border-radius:44px 0 0 0;background:linear-gradient(180deg,var(--green) 0%,var(--green-light) 100%);color:#fff;padding:18px 0 0 32px}
  .phone{font-weight:600;font-size:24px;line-height:30px}
  .contact-panel .lines{margin-top:12px;font-size:11px;line-height:14.5px}
  .contact-panel .addr{margin-top:11px;font-size:11px;line-height:14.5px}

  /* back */
  .services-title{left:20px;top:14px;color:var(--green);font-weight:700;font-size:27px;letter-spacing:.3px}
  .service{width:217px;border-radius:6px;padding:8px 10px;color:#fff}
  .service--dark{background:var(--green)}
  .service--light{background:var(--green-light)}
  .service h3{font-weight:600;font-size:19px;line-height:24px;margin-bottom:8px}
  .service p{font-size:7.6px;line-height:11.6px}
  .photos{left:0;top:316px}
  .address-line{left:600px;width:222px;height:1.4px;background:var(--rule)}
  .back-contact{right:30px;top:420px;text-align:right;font-size:10.8px;line-height:14px}
  .back-contact .phone{color:var(--green);margin-bottom:10px}
  .back-contact .addr{margin-top:12px}
</style>
</head>
<body>

<section class="card card--front">
  <svg class="abs hero-bg" width="840" height="362" viewBox="0 0 840 362" role="img" aria-label="Photo of the clinic reception area with a green tint">
    <defs>
      <linearGradient id="heroTone" x1="0" y1="0" x2="1" y2="1">
        <stop offset="0" stop-color="#3a9a58"/>
        <stop offset=".55" stop-color="#4f9e64"/>
        <stop offset="1" stop-color="#6fb47a"/>
      </linearGradient>
    </defs>
    <rect width="840" height="362" fill="url(#heroTone)"/>
    <path d="M0 0 H245 C220 40 215 104 160 104 H0 Z" fill="#fff"/>
  </svg>
  <div class="abs doctor" role="img" aria-label="Photo of the smiling pediatric dentist with arms crossed"></div>
  <div class="abs brand brand--front"><span class="brand-dot"></span><span class="brand-name">Birchwood<br>Pediatric Dentistry</span></div>
  <h1 class="abs headline">LET YOUR<br>SMILE GROW!</h1>
  <p class="abs subhead">A dental home for your CHILD'S SMILE in MILLBROOK, OAKRIDGE,<br>CEDAR FALLS, LINDEN, ASHFORD AND MORE.</p>
  <p class="abs intro">At Birchwood Pediatric Dentistry, our ultimate goal is to make sure our patients feel comforted, listened to, and taken care of. We dedicate our effort and time to creating a positive experience that leaves a lasting impression on our young patients.</p>

  <h2 class="abs network-title">WE ARE IN-NETWORK WITH THE FOLLOWING PROVIDERS:</h2>
  <ul class="abs providers providers--a">
    <li>Northstar Health Shield</li>
    <li>Linkway Dental</li>
    <li>Veridian Care</li>
    <li>Sentinel Mutual</li>
    <li>Lifeline PDP Plus</li>
    <li>Unity Health Partners</li>
    <li>Harbor Dental Premier (not Harbor Dental PPO)</li>
  </ul>
  <ul class="abs providers providers--b">
    <li>Carewell</li>
    <li>Daybreak Life</li>
    <li>Amerival</li>
    <li>Humanis Health</li>
    <li>Keystone Benefits</li>
    <li>StateCare Kids (Medicaid)</li>
    <li>Pinnacle DPPO only (not Pinnacle Advantage)</li>
  </ul>

  <div class="abs contact-panel">
    <div class="phone">+1 555-014-2380</div>
    <div class="lines">hello@birchwoodsmiles.com<br>birchwoodsmiles.com</div>
    <div class="addr">48 Harbor Lane, Suite 210, Millbrook,<br>CT, United States, 06000</div>
  </div>
</section>

<section class="card card--back">
  <h2 class="abs services-title">OUR FEATURED SERVICES</h2>

  <article class="abs service service--dark" style="left:20px;top:58px;height:122px">
    <h3>Dental Cleanings</h3>
    <p>Our gentle and skilled team of dental professionals ensures that each dental cleaning is a fun and positive experience. With our specialized approach, your little ones will develop a lifelong commitment to excellent dental hygiene, setting the foundation for healthy smiles that last a lifetime.</p>
  </article>
  <article class="abs service service--light" style="left:243px;top:58px;height:122px">
    <h3>Dental Emergencies</h3>
    <p>When your child experiences a dental accident, it can be scary and overwhelming. That's why we offer emergency pediatric dentistry to treat your child's injury and relieve their pain, so they can get back to smiling with confidence.</p>
  </article>
  <article class="abs service service--light" style="left:20px;top:186px;height:122px">
    <h3>Dental Sedation</h3>
    <p>We understand most children can feel anxious or scared when visiting the dentist. Whether it's a routine appointment or dental surgery, we provide a variety of dental sedation options so both you and your child can feel calm and in good hands.</p>
  </article>
  <article class="abs service service--dark" style="left:243px;top:186px;height:122px">
    <h3>Dental Fillings</h3>
    <p>Cavities are common among kids and can cause pain, infection, or even tooth loss when not properly treated. We offer a variety of affordable, simple, and long-lasting dental fillings so your child's teeth can stay healthy as they develop and grow out of their baby teeth.</p>
  </article>

  <svg class="abs photos" width="580" height="244" viewBox="0 0 580 244">
    <path d="M0 0 H470 C490 0 500 8 508 24 L572 244 H0 Z" fill="var(--green-mid)"/>
    <rect x="0" y="6" width="200" height="114" fill="#c7b3a8" role="img" aria-label="Photo of two team members smiling together"/>
    <rect x="0" y="126" width="200" height="118" fill="#8c93b5" role="img" aria-label="Photo of children sitting on a classroom rug"/>
    <path d="M206 6 H466 C480 6 488 14 494 28 L556 244 H206 Z" fill="#b6a892" role="img" aria-label="Photo of a dentist reading a picture book to young children"/>
  </svg>

  <div class="abs brand brand--back"><span class="brand-dot"></span><span class="brand-name">Birchwood<br>Pediatric Dentistry</span></div>
  <div class="abs address-line" style="top:158px"></div>
  <div class="abs address-line" style="top:202px"></div>
  <div class="abs address-line" style="top:246px"></div>
  <div class="abs address-line" style="top:290px"></div>

  <div class="abs back-contact">
    <div class="phone">+1 555-014-2380</div>
    <div>hello@birchwoodsmiles.com<br>birchwoodsmiles.com</div>
    <div class="addr">48 Harbor Lane, Suite 210, Millbrook,<br>CT, United States, 06000</div>
  </div>
</section>

</body>
</html>
```